Corporate-Design für Zahnarztpraxis
Zielgruppe
Ich bin Zahnärztin in einer Einzelbehandler Praxis. Die Praxis liegt im ländlichen Gebiet am Rand von Berlin. Zielgruppe sind neue Patienten jeglichen Alters. Die Praxis zeichnet sich durch eine familiäre vertrauenesvolle Atmosphäre im Umgang mit den Patienten aus.
Aufgabenstellung
- weibliches Erscheinungsbild
- warme Farben
- Vertrauen
- bei Verwendung eines Zahns als Symbols sollte dieser indirekt dargestellt werden, eventuell die Form eines Zahnes aufgreifen

```html
<!DOCTYPE html>
<html lang="de">
<head>
<meta charset="utf-8">
<title>Lena Marwitz – Corporate Design</title>
<link href="https://fonts.googleapis.com/css2?family=Cormorant+Garamond:wght@500&family=Montserrat:wght@400;500&display=swap" rel="stylesheet">
<style>
:root{
  --rose:#c47d95;
  --rose-soft:#e8a3a6;
  --name:#bf6f8a;
  --cream:#fbf9f6;
  --paper:#ffffff;
  --ink:#8a7f84;
  --window:#eeeded;
}
*{margin:0;padding:0;box-sizing:border-box}
html,body{width:1200px;height:1093px;overflow:hidden}
body{position:relative;font-family:"Montserrat",sans-serif;color:var(--ink);
  background:linear-gradient(120deg,#ede3e3 0%,#e6e3e8 45%,#ece6e6 75%,#efe7e2 100%)}
.abs{position:absolute}
.top-band{left:0;top:0;width:1200px;height:162px;background:var(--cream);box-shadow:0 3px 8px rgba(0,0,0,.25)}
.bottom-band{left:0;top:933px;width:1200px;height:160px;background:var(--rose)}
.mark{display:flex;align-items:center;gap:.35em;font-family:"Cormorant Garamond",serif;font-weight:500;color:var(--name);white-space:nowrap;letter-spacing:.02em;line-height:1}
.mark::before{content:"";width:.8em;height:.8em;border-radius:50%;border:.08em solid currentColor;flex:none}
.mark.no-dot::before{display:none}
.mark.light{color:#fff}
.hero-mark{font-size:44px}
.sheet{background:var(--paper);box-shadow:2px 3px 6px rgba(80,60,70,.35)}
.label{font-size:14px;color:#444}
.fold{left:0;width:8px;height:1px;background:#bbb}
.ghost{border-radius:50%;background:radial-gradient(circle,rgba(196,125,149,.06),rgba(196,125,149,0) 70%)}
.tiny{font-size:4.2px;line-height:1.3;color:var(--ink);white-space:nowrap}
.contact-row{display:flex;align-items:center;gap:3px}
.ico{width:5px;height:5px;border-radius:1px;background:var(--rose);flex:none}
.footer-rule{height:2px;background:var(--rose-soft)}
.foot-col{padding-left:5px;border-left:1px solid var(--rose)}
.card{width:114px;height:73px;background:var(--paper);box-shadow:1px 2px 4px rgba(80,60,70,.3);overflow:hidden}
.card .mark{font-size:7px}
.card .tiny{font-size:3.6px}
.card .ico{width:4px;height:4px;border-radius:1px}
.card.cream{background:var(--cream)}
.card.rose{background:var(--rose)}
.envelope{width:296px;height:147px;background:var(--paper);box-shadow:2px 3px 6px rgba(80,60,70,.35)}
.window{left:26px;top:60px;width:121px;height:61px;border-radius:4px;background:var(--window)}
</style>
</head>
<body>

<header class="abs top-band">
  <div class="abs mark hero-mark" style="left:445px;top:62px">LENA MARWITZ</div>
</header>

<!-- Letterheads -->
<span class="abs label" style="left:44px;top:455px">1</span>
<section class="abs sheet" style="left:58px;top:262px;width:283px;height:399px">
  <div class="abs mark" style="left:80px;top:18px;font-size:13px">LENA MARWITZ</div>
  <div class="abs tiny" style="left:210px;top:76px">
    <div class="contact-row"><span class="ico"></span>+000 12345 6789</div>
    <div class="contact-row"><span class="ico"></span>urname@email.com</div>
    <div class="contact-row"><span class="ico"></span>urwebsitename.com</div>
    <div class="contact-row"><span class="ico"></span>Street Address Here</div>
  </div>
  <span class="abs fold" style="top:143px"></span><span class="abs fold" style="top:201px"></span><span class="abs fold" style="top:284px"></span>
  <div class="abs ghost" role="img" aria-label="Blasses Markenzeichen als Hintergrund" style="left:80px;top:150px;width:130px;height:130px"></div>
  <div class="abs footer-rule" style="left:27px;top:356px;width:256px"></div>
  <div class="abs tiny" style="left:27px;top:363px">Registerinformationen<br>Sitz: Xxxxxx<br>Registergericht: Xxxxxx<br>Registernummer: HRB Xxxx</div>
  <div class="abs tiny foot-col" style="left:103px;top:363px">Bankverbindung<br>IBAN: DEXX XXXX XXXX XXXX<br>BIC XXXXXXXXXXX<br>Bank: Xxxxxx</div>
  <div class="abs tiny foot-col" style="left:213px;top:363px">Umsatzsteuer ID<br>DEX XXXXXX</div>
</section>

<span class="abs label" style="left:391px;top:455px">2</span>
<section class="abs sheet" style="left:406px;top:262px;width:283px;height:399px">
  <div class="abs mark" style="left:26px;top:27px;font-size:13px">LENA MARWITZ</div>
  <div class="abs tiny" style="left:210px;top:26px">Company adress<br>+000 12345 6789<br>+000 12345 6789<br>urname@email.com<br>urwebsitename.com</div>
  <span class="abs fold" style="top:143px"></span><span class="abs fold" style="top:201px"></span><span class="abs fold" style="top:284px"></span>
  <div class="abs ghost" role="img" aria-label="Blasses Markenzeichen als Hintergrund" style="left:85px;top:145px;width:130px;height:130px"></div>
  <div class="abs tiny" style="left:32px;top:362px">Registerinformationen<br>Sitz: Xxxxxx<br>Registergericht: Xxxxxx<br>Registernummer: HRB Xxxx</div>
  <div class="abs tiny foot-col" style="left:106px;top:362px">Bankverbindung<br>IBAN: DEXX XXXX XXXX XXXX<br>BIC XXXXXXXXXXX<br>Bank: Xxxxxx</div>
  <div class="abs tiny foot-col" style="left:218px;top:362px">Umsatzsteuer ID<br>DEX XXXXXX</div>
</section>

<!-- Business cards -->
<div class="abs card cream" style="left:767px;top:292px;border-top:4px solid var(--rose);border-bottom:4px solid var(--rose)"><div class="abs mark" style="left:24px;top:28px">LENA MARWITZ</div></div>
<div class="abs card cream" style="left:912px;top:292px;border:3px solid var(--rose)"><div class="abs mark" style="left:22px;top:30px">LENA MARWITZ</div></div>
<div class="abs card" style="left:1058px;top:292px;border:3px solid var(--rose)">
  <div class="abs ghost" style="left:70px;top:4px;width:30px;height:30px;background:rgba(196,125,149,.12)"></div>
  <div class="abs" style="left:12px;top:37px;font-size:5.5px;font-weight:500;color:var(--name);white-space:nowrap">Name Surname</div>
  <div class="abs tiny" style="left:12px;top:44px">POSITION</div>
  <div class="abs tiny" style="left:10px;top:53px"><div class="contact-row"><span class="ico"></span>+000 12345 6789</div><div class="contact-row"><span class="ico"></span>Street Address Here</div></div>
  <div class="abs tiny" style="left:60px;top:53px"><div class="contact-row"><span class="ico"></span>urname@email.com</div><div class="contact-row"><span class="ico"></span>urwebsitename.com</div></div>
</div>

<div class="abs card" style="left:767px;top:375px">
  <svg class="abs" style="left:0;top:0" width="114" height="74"><polygon points="48,0 114,0 114,74 32,74" fill="var(--rose)"/></svg>
  <div class="abs" style="left:20px;top:32px;width:8px;height:8px;border-radius:50%;border:1px solid var(--rose)"></div>
  <div class="abs mark light no-dot" style="left:50px;top:32px">LENA MARWITZ</div>
</div>
<div class="abs card rose" style="left:912px;top:375px;border-bottom:4px solid #fff">
  <div class="abs" style="left:41px;top:22px;width:32px;height:32px;border-radius:50%;border:1px solid rgba(255,255,255,.7)"></div>
</div>
<div class="abs card" style="left:1058px;top:375px">
  <div class="abs mark" style="left:56px;top:8px;font-size:5.5px">LENA MARWITZ</div>
  <div class="abs" style="left:7px;top:33px;font-family:'Cormorant Garamond',serif;font-size:6px;color:var(--name);white-space:nowrap">NAME SURNAME</div>
  <div class="abs tiny" style="left:7px;top:39px">Position</div>
  <div class="abs" style="left:7px;top:45px;width:100px;height:1px;background:var(--rose)"></div>
  <div class="abs tiny" style="left:7px;top:48px"><div>+000 12345 6789</div><div>+000 12345 6789</div><div>urname@email.com</div><div>urwebsitename.com</div></div>
  <div class="abs tiny" style="left:66px;top:56px">Street Address Here</div>
</div>

<div class="abs card" style="left:767px;top:463px"><div class="abs mark" style="left:30px;top:30px;font-size:6px">LENA MARWITZ</div></div>
<div class="abs card" style="left:912px;top:463px;border-left:4px solid var(--rose-soft);border-right:4px solid var(--rose-soft)"><div class="abs mark" style="left:18px;top:30px">LENA MARWITZ</div></div>
<div class="abs card" style="left:1058px;top:463px;border-left:4px solid var(--rose-soft)">
  <div class="abs mark" style="left:32px;top:8px;font-size:6px">LENA MARWITZ</div>
  <div class="abs" style="left:32px;top:33px;font-size:5px;color:var(--name);white-space:nowrap">NAME SURNAME</div>
  <div class="abs tiny" style="left:44px;top:40px">Position</div>
  <div class="abs tiny" style="left:10px;top:52px">+000 12345 6789<br>+000 12345 6789<br>urname@email.com</div>
  <div class="abs tiny" style="left:64px;top:56px">Street Address Here</div>
</div>

<div class="abs card" style="left:767px;top:549px">
  <div class="abs" style="left:0;top:0;width:35px;height:73px;background:var(--rose)"></div>
  <div class="abs" style="left:22px;top:25px;width:24px;height:24px;border-radius:50%;border:1px solid #fff;background:var(--rose)"></div>
  <div class="abs mark" style="left:50px;top:33px;font-size:6px">LENA MARWITZ</div>
</div>
<div class="abs card" style="left:909px;top:549px;border-bottom:3px solid #c9a3c4"><div class="abs mark" style="left:20px;top:30px">LENA MARWITZ</div></div>
<div class="abs card" style="left:1058px;top:549px;border-bottom:3px solid #c9a3c4">
  <div class="abs" style="left:14px;top:6px;width:18px;height:18px;border-radius:50%;border:1px solid var(--rose-soft)"></div>
  <div class="abs" style="left:62px;top:30px;font-size:5px;color:var(--name);white-space:nowrap">NAME SURNAME</div>
  <div class="abs tiny" style="left:90px;top:36px">Position</div>
  <div class="abs" style="left:0;top:42px;width:114px;height:1px;background:var(--rose)"></div>
  <div class="abs tiny" style="left:10px;top:47px;line-height:1.15">+000 12345 6789<br>+000 12345 6789<br>urname@email.com<br>urwebsitename.com<br>Street Address Here</div>
</div>

<!-- Envelopes -->
<span class="abs label" style="left:219px;top:774px">1</span>
<section class="abs envelope" style="left:240px;top:697px;border-bottom:3px solid var(--rose-soft)">
  <div class="abs mark" style="left:28px;top:32px;font-size:13px">LENA MARWITZ</div>
  <div class="abs window"></div>
  <div class="abs tiny" style="left:230px;top:107px">Company adress<br>+000 12345 6789<br>urwebsitename.com</div>
</section>
<span class="abs label" style="left:572px;top:774px">2</span>
<section class="abs envelope" style="left:594px;top:697px;border-bottom:3px solid var(--rose)">
  <div class="abs mark" style="left:24px;top:34px;font-size:13px">LENA MARWITZ</div>
  <div class="abs window" style="left:23px"></div>
  <div class="abs" style="left:232px;top:83px;width:42px;height:42px;border-radius:50%;border:2px solid #c9a3c4"></div>
</section>

<div class="abs mark" style="left:986px;top:858px;font-size:21px">LENA MARWITZ</div>

<footer class="abs bottom-band">
  <div class="abs mark light hero-mark" style="left:445px;top:50px">LENA MARWITZ</div>
</footer>

</body>
</html>
```